New School header and footer

Our school needs a modern new header and a matching footer. Currently we have the school logo, name and contact with no graphics at all (attached).
I have also attached another version of the school logo which is on our school sign.
The school's logo is a Swift (Apus pacificus) (bird) see http://www.findlyweb.example/search?q=swift+bird+images

The school is located in North Queensland Australia near the town of Ingham it was established in 1922

I would like the header/footer to have:
The school name- Marrelda State School
School moto - Courage beside kindness
contact details: Address Phone Fax website and principal email (some of these things could be in the footer) these details are in the uploaded files
The logo or elements of the logo (as is or modified to modernise)

School website is https://marreldass.qlx.edu.example

The header and footer would be used on A4 paper with microsoft word it will be used for the school newsletter and in all official school documents.

It can be colour or black and white. School uniforms are have light blue some dark blue and white the colours in the design are not limited to these colours.
Updates

Thanks to those people who have already submitted designs. I have made some additions to the brief in the should have and should not have sections and also the sliding scale thing. I hope that helps.

There are a lot of designs thankyou all so much. Some feedback from my staff is that we really need to keep the traditional logo of the bird from the website. It doesn't have to have the words around it but the shape and position needs to stay the same. I thought we were ready to change modernise the logo but unfortunately they aren't ready. However the rest of the design needs to be modern, less rigid and square. There is one square design that I did like and they have made the changes required. I will choose the designs I like and should be putting them up for online voting next week.
Just a side note a large tropical cyclone is moving close to our community. We are not at risk right now but it is possible that we will experience flooding and maybe loss of power so if there is a delay in posting the results this will probably be the reason.  I will try to respond to last minute questions or design submissions but I'll be pretty busy preparing my home and the school for the possibility of this weather event. Once again thankyou for your submissions I have been impressed by the quailty of the submissions from this particular design crowd.

Target Market(s)

For a school used in official documents, letters, and newsletters.

My staff will be choosing the winner.

Industry/Entity Type

School

Requirements
Must have
• School name
School motto
Address
Phone
Fax
Website URL
Header and footer
Should not have
• Avoid large amounts of block colours this letter head will be used in colour format most of the time but will be photo copied and faxed from time to time.

```html
<!DOCTYPE html>
<html lang="en">
<head>
<meta charset="utf-8">
<title>Marrelda State School – Letterhead</title>
<link href="https://fonts.googleapis.com/css2?family=Exo+2:ital,wght@0,400;0,600;1,600&display=swap" rel="stylesheet">
<style>
  :root {
    --backdrop: #ececec;
    --paper: #ffffff;
    --navy: #2f3c7e;
    --sky: #4f63b5;
    --ink: #4a4a4a;
    --muted: #6a6a6a;
  }
  * { box-sizing: border-box; margin: 0; padding: 0; }
  html, body {
    width: 1200px; height: 1000px; overflow: hidden;
    background: var(--backdrop);
    font-family: "Exo 2", sans-serif;
  }
  .letterhead {
    position: absolute; left: 270px; top: 33px;
    width: 660px; height: 934px;
    background: var(--paper);
    box-shadow: 0 2px 10px rgba(0,0,0,.08);
  }
  .masthead {
    position: absolute; top: 46px; left: 0; right: 0;
    display: flex; flex-direction: column; align-items: center;
  }
  .masthead-mark {
    width: 86px; height: 86px; border-radius: 50%;
    background: var(--navy);
  }
  .school-name {
    margin-top: 8px;
    font-size: 17px; font-weight: 600; color: var(--navy);
    letter-spacing: .3px; text-transform: uppercase;
  }
  .school-motto {
    font-size: 11px; font-style: italic; color: var(--ink);
    margin-top: 1px;
  }
  .letter {
    position: absolute; top: 208px; left: 70px; right: 70px;
    font-size: 11px; line-height: 1.55; color: var(--ink);
  }
  .letter-title {
    text-align: right; color: var(--navy);
    font-size: 17px; font-weight: 600; font-style: italic;
    margin: -4px 0 10px;
  }
  .salutation { margin-bottom: 6px; }
  .letter p.body { text-align: justify; margin-bottom: 26px; }
  .sign-off { margin-top: -14px; }
  .signature {
    position: absolute; left: 420px; top: 640px;
    width: 110px; height: 40px;
    background: linear-gradient(90deg, #efefef, #f7f7f7);
    border-radius: 4px;
  }
  .signatory {
    position: absolute; left: 420px; top: 684px;
    font-size: 11px; color: var(--ink);
  }
  .footer {
    position: absolute; left: 0; right: 0; bottom: 40px; height: 70px;
    font-size: 9px; color: var(--muted);
  }
  .footer-band-light {
    position: absolute; left: 0; top: 28px; width: 150px; height: 4px;
    background: var(--sky);
  }
  .footer-band-dark {
    position: absolute; left: 160px; right: 0; bottom: 0; height: 5px;
    background: var(--navy);
  }
  .footer-divider {
    position: absolute; left: 160px; top: 30px; width: 1px; height: 32px;
    background: #bcbcbc;
  }
  .contact-list { position: absolute; list-style: none; }
  .contact-list li { display: flex; align-items: center; gap: 5px; line-height: 1.35; }
  .contact-list svg { width: 8px; height: 8px; fill: var(--navy); flex: none; }
  .contact-location { left: 30px; top: -8px; }
  .contact-reach { left: 170px; top: 30px; }
</style>
</head>
<body>
<main class="letterhead">
  <header class="masthead">
    <div class="masthead-mark"></div>
    <div class="school-name">Marrelda State School</div>
    <div class="school-motto">Courage beside kindness</div>
  </header>

  <article class="letter">
    <p class="salutation">Dear Parent,</p>
    <h1 class="letter-title">Lorem ipsum dolor sit ametconsectetur.</h1>
    <p class="body">Lorem ipsum dolor sit amet, consectetur adipiscing elit. Nulla sodales nisi vitae lorem ipsum dolor sit amet, consectetur adipiscing elit. Suspendisse feugiat eros nisi, a facilisis risus eleifend sed. Aliquam mauris enim, fermentum eu lacinia sit amet, laoreet eu leo. Nullam eleifend nulla in libero tristique, ac vulputate odio tincidunt. Etiam non condimentum tortor. Integer suscipit neque nec odio porttitor cursus. Phasellus a sapien blandit, suscipit justo id, condimentum ante. Morbi tristique justo risus, id mattis dui molestie ut. Nullam volutpat ut quam commodo faucibus. Pellentesque urna est, interdum in elit quis, pharetra elementum orci. Nam pharetra velit molestie justo placerat scelerisque.</p>
    <p class="body">Nulla tincidunt molestie libero vel pretium. Donec condimentum nulla sit amet risus semper imperdiet. Duis congue eros nec diam blandit, et pellentesque sapien auctor. Curabitur iaculis enim lectus, in imperdiet mauris mattis eget. Etiam ac ornare metus. Mauris risus leo, egestas at dolor a, ultrices adipiscing est. Nunc faucibus scelerisque mollis. Pellentesque aliquet mauris tellus, id dignissim risus viverra et. Mauris venenatis lobortis eros. Nam id diam in ligula malesuada feugiat. Cras turpis felis, aliquet id mauris elementum, feugiat ultricies nisl.</p>
    <p class="body">Nullam auctor venenatis metus, eu pulvinar sapien dapibus non. Cum sociis natoque penatibus et magnis dis parturient montes, nascetur ridiculus mus. Praesent sed lorem eget tortor volutpat dictum vel vel ipsum. Morbi ac mauris sed elit dictum volutpat. Morbi pulvinar non nisi in ultrices. Pellentesque quis mi in risus eleifend adipiscing.</p>
    <p class="sign-off">Best regards,</p>
  </article>

  <div class="signature" role="img" aria-label="Handwritten signature of the principal"></div>
  <div class="signatory">Alan Pryce</div>

  <footer class="footer">
    <ul class="contact-list contact-location">
      <li><svg viewBox="0 0 10 10"><path d="M5 0a3.5 3.5 0 0 0-3.5 3.5C1.5 6 5 10 5 10s3.5-4 3.5-6.5A3.5 3.5 0 0 0 5 0zm0 5a1.5 1.5 0 1 1 0-3 1.5 1.5 0 0 1 0 3z"/></svg>Carrow Road</li>
      <li><svg viewBox="0 0 10 10"></svg>Pelling QLD 4899</li>
      <li><svg viewBox="0 0 10 10"><circle cx="5" cy="5" r="4.2" fill="none" stroke="#2f3c7e" stroke-width="1.2"/><path d="M1 5h8M5 1c-2 2.5-2 5.5 0 8M5 1c2 2.5 2 5.5 0 8" fill="none" stroke="#2f3c7e" stroke-width=".9"/></svg>https://marreldass.qlx.edu.example</li>
    </ul>
    <div class="footer-band-light"></div>
    <div class="footer-divider"></div>
    <ul class="contact-list contact-reach">
      <li><svg viewBox="0 0 10 10"><path d="M2 0l2 2.5-1 1.5c.6 1.3 1.6 2.3 3 3l1.5-1L10 8 8.5 10C4 9.5.5 6 0 1.5z"/></svg>(07) 5550 1824</li>
      <li><svg viewBox="0 0 10 10"><rect x="0" y="3" width="10" height="6" rx="1"/><rect x="2.5" y="0" width="5" height="3"/></svg>(07) 5550 1825</li>
      <li><svg viewBox="0 0 10 10"><rect x="0" y="1.5" width="10" height="7" rx="1"/><path d="M0.5 2l4.5 3.5L9.5 2" fill="none" stroke="#fff" stroke-width="1"/></svg>the.principal@marreldass.qlx.edu.example</li>
    </ul>
    <div class="footer-band-dark"></div>
  </footer>
</main>
</body>
</html>
```